Dental Practice Billboard Design

We are a newer dental practice in need of a simple but appealing billboard for our growing dental practice to attract new patients. The practice is owned by husband and wife dentists and is family friendly in a small town in Kentucky. We try to be very friendly and caring to our patients. Would prefer a blue background for the billboard and our tooth logo to be prominent. We are partial to the Patua One font used in the image below but please feel free to tweak it as you deem necessary. The shape of the uppercase D and lowercase g are why we like that font, so fonts with a similarly shaped “D” and “g” would work as well. Please include our phone number (606) 847-3962. Please see our website Harlowfamilydentistry.com for more info on the practice if needed. Thank you! Looking forward to seeing your creation.
Updates

The dimensions will be 12ft x 24ft (3.6576m x 7.3152m). Apologies for not including this in the original prompt. Thank you all for your submissions.

Industry/Entity Type

Dental

Font styles to use
Other font styles liked:
• Patua One

Colors
0054AA
0677BA
7BADD7
CADEEF
E8F1F8
0094D4
00A9DD
6FCCEA
C7EBF8
E9F6FB
00AB8E
00BBA5
67D7C9
C6EFE9
E9F9F6
59FF00
82FF00
B8FF75
E3FFCB
F4FFEA

Requirements
Must have
• Phone number, website, Logo, Practice name “Harlow Family Dentistry”
Should not have
• A tagline or slogan

```html
<!DOCTYPE html>
<html lang="en">
<head>
<meta charset="utf-8">
<title>Harlow Family Dentistry Billboard</title>
<link rel="stylesheet" href="https://fonts.googleapis.com/css2?family=Patua+One&display=swap">
<style>
  :root {
    --brand-blue: #0054aa;
    --brand-navy: #0b2a5c;
    --brand-green: #16b31c;
    --paper: #ffffff;
    --stage: #e8f1f8;
    --photo-light: #e9ddd0;
    --photo-mid: #b8a08a;
    --photo-dark: #6d5747;
  }
  * { box-sizing: border-box; margin: 0; padding: 0; }
  html, body {
    width: 1200px;
    height: 730px;
    overflow: hidden;
    background: var(--stage);
  }
  .billboard {
    position: absolute;
    left: 20px;
    top: 75px;
    width: 1160px;
    height: 580px;
    overflow: hidden;
    background: var(--brand-blue);
    font-family: "Patua One", Georgia, serif;
  }
  .billboard-shapes {
    position: absolute;
    inset: 0;
  }
  .practice-name {
    position: absolute;
    left: 40px;
    top: 120px;
    display: flex;
    align-items: center;
    gap: 26px;
    color: var(--paper);
  }
  .name-mark {
    width: 120px;
    height: 120px;
    border-radius: 50%;
    background: var(--brand-green);
    flex: none;
  }
  .name-text { line-height: 1; }
  .name-primary {
    display: block;
    font-size: 112px;
    letter-spacing: 1px;
  }
  .name-secondary {
    display: block;
    font-size: 48px;
    margin-top: 6px;
    padding-left: 4px;
  }
  .contact {
    position: absolute;
    left: 36px;
    top: 448px;
    color: var(--brand-navy);
  }
  .contact-line {
    display: flex;
    align-items: center;
    gap: 14px;
  }
  .contact-phone { font-size: 74px; line-height: 1; }
  .contact-web { font-size: 40px; line-height: 1; margin-top: 10px; }
  .contact-icon { flex: none; }
</style>
</head>
<body>
  <main class="billboard">
    <svg class="billboard-shapes" width="1160" height="580" viewBox="0 0 1160 580" aria-hidden="true">
      <rect class="contact-band" x="0" y="420" width="820" height="160" fill="var(--paper)"/>
      <path class="photo-frame" d="M745,0 C690,170 700,420 770,580 L1160,580 L1160,0 Z" fill="var(--paper)"/>
      <path class="photo-edge" d="M772,0 C720,170 728,420 796,580" fill="none" stroke="var(--brand-blue)" stroke-width="6"/>
      <path class="accent-band" d="M1080,0 L1160,0 L1160,580 L1110,580 C1140,400 1140,170 1080,0 Z" fill="var(--brand-green)"/>
    </svg>

    <svg style="position:absolute;left:0;top:0" width="1160" height="580" viewBox="0 0 1160 580" role="img" aria-label="Photo of the two smiling dentists in white coats">
      <defs>
        <linearGradient id="photoTone" x1="0" y1="0" x2="1" y2="1">
          <stop offset="0" stop-color="var(--photo-light)"/>
          <stop offset="0.6" stop-color="var(--photo-mid)"/>
          <stop offset="1" stop-color="var(--photo-dark)"/>
        </linearGradient>
      </defs>
      <path d="M790,30 C745,190 752,420 812,580 L1098,580 C1120,400 1118,190 1066,30 Z" fill="url(#photoTone)"/>
    </svg>

    <h1 class="practice-name">
      <span class="name-mark" aria-hidden="true"></span>
      <span class="name-text">
        <span class="name-primary">Harlow</span>
        <span class="name-secondary">Family Dentistry</span>
      </span>
    </h1>

    <div class="contact">
      <p class="contact-line contact-phone">
        <svg class="contact-icon" width="38" height="38" viewBox="0 0 24 24" aria-hidden="true">
          <path d="M6.6 10.8a15.1 15.1 0 0 0 6.6 6.6l2.2-2.2a1 1 0 0 1 1-.25 11.4 11.4 0 0 0 3.6.57 1 1 0 0 1 1 1V20a1 1 0 0 1-1 1A17 17 0 0 1 3 4a1 1 0 0 1 1-1h3.5a1 1 0 0 1 1 1c0 1.25.2 2.45.57 3.57a1 1 0 0 1-.25 1z" fill="var(--brand-green)"/>
        </svg>
        (606) 847-3962
      </p>
      <p class="contact-line contact-web">
        <svg class="contact-icon" width="36" height="36" viewBox="0 0 24 24" aria-hidden="true" fill="none" stroke="var(--brand-green)" stroke-width="2">
          <circle cx="12" cy="12" r="10"/>
          <ellipse cx="12" cy="12" rx="4.5" ry="10"/>
          <line x1="2" y1="12" x2="22" y2="12"/>
          <line x1="4" y1="7" x2="20" y2="7"/>
          <line x1="4" y1="17" x2="20" y2="17"/>
        </svg>
        Harlowfamilydentistry.com
      </p>
    </div>
  </main>
</body>
</html>
```